Business Card Design

We recently had a new logo designed by Pixel Harbor. Now we want to create new business cards and letterhead that compliment our new logo.

We are audiologists in private practice specializing in hearing evaluations and fitting hearing aids. We want a clean and professional card.

We need business cards for each audiologist. The names and titles are:
Marnie Ostrova, AuD
Audiologist

Jen Tarbel, AuD
Audiologist

Corvina Plesk, AuD
Audiologist

We also need a business card with no provider. Just a generic one.

Finally, we need an appointment card. This is what the front desk uses to give to the patient with their next appointment date and time.

Target Market(s)

Our clients tend to be highly educated. They are older so the cards should be clean and easy to read. No squirrely font please.

Industry/Entity Type

Business

Contact Information for Business Card

20731 8th Ave NE, suite 417
Seattle, WA 98177
206-592-8074

Requirements
Must have
• Clean
Easy to read
Professional
Modern but approachable / warm
Should not have
• Other pictures besides the logo

```html
<!DOCTYPE html>
<html lang="en">
<head>
<meta charset="utf-8">
<title>Business Card – Marnie Ostrova</title>
<link href="https://fonts.googleapis.com/css2?family=Carlito:wght@400;700&display=swap" rel="stylesheet">
<style>
  :root {
    --backdrop: #3b3b3b;
    --card: #ffffff;
    --navy: #164766;
    --name: #1d4868;
    --teal-rule: #7fa9a6;
    --teal: #5fb3a6;
    --text-grey: #6a6a6a;
    --icon-blue: #1f6b93;
  }
  * { margin: 0; padding: 0; box-sizing: border-box; }
  html, body {
    width: 1200px;
    height: 1000px;
    overflow: hidden;
    background: var(--backdrop);
    font-family: "Carlito", "Calibri", Arial, sans-serif;
  }
  .business-card {
    position: absolute;
    left: 200px;
    top: 283px;
    width: 793px;
    height: 464px;
    background: var(--card);
  }
  .edge-band {
    position: absolute;
    left: 0;
    top: 0;
    width: 16px;
    height: 100%;
    background: var(--navy);
  }
  .brand {
    position: absolute;
    left: 88px;
    top: 82px;
    display: flex;
    align-items: center;
    gap: 14px;
  }
  .brand-dot {
    width: 60px;
    height: 60px;
    border-radius: 50%;
    background: var(--navy);
  }
  .brand-name {
    font-size: 24px;
    font-weight: 700;
    color: var(--navy);
    line-height: 1.1;
    width: 200px;
  }
  .provider-name {
    position: absolute;
    right: 63px;
    top: 240px;
    font-size: 29px;
    font-weight: 700;
    color: var(--name);
    letter-spacing: 0.2px;
  }
  .divider {
    position: absolute;
    left: 112px;
    top: 295px;
    width: 455px;
    height: 2px;
    background: var(--teal-rule);
  }
  .provider-title {
    position: absolute;
    right: 63px;
    top: 283px;
    font-size: 17px;
    color: var(--text-grey);
  }
  .contact-list {
    position: absolute;
    right: 59px;
    top: 346px;
    list-style: none;
    text-align: right;
    font-size: 17px;
    color: var(--text-grey);
    line-height: 25px;
  }
  .contact-list li {
    display: flex;
    justify-content: flex-end;
    align-items: center;
    gap: 9px;
  }
  .contact-icon {
    width: 16px;
    height: 16px;
    fill: var(--icon-blue);
  }
</style>
</head>
<body>
  <div class="business-card">
    <div class="edge-band"></div>

    <div class="brand">
      <div class="brand-dot"></div>
      <div class="brand-name">Lakeview Hearing Services</div>
    </div>

    <div class="provider-name">Marnie Ostrova</div>
    <div class="divider"></div>
    <div class="provider-title">AuD, Audiologist</div>

    <ul class="contact-list">
      <li>
        <span>20731 8th Ave NE, suite 417 Seattle, WA 98177</span>
        <svg class="contact-icon" viewBox="0 0 16 16" aria-hidden="true">
          <path d="M8 1 L15.5 8 L13.5 8 L13.5 15 L9.8 15 L9.8 10.5 L6.2 10.5 L6.2 15 L2.5 15 L2.5 8 L0.5 8 Z"/>
        </svg>
      </li>
      <li>
        <span>206-592-8074</span>
        <svg class="contact-icon" viewBox="0 0 16 16" aria-hidden="true">
          <path d="M3.6 1.2 L5.8 1 L7.2 4.6 L5.6 5.9 C6.4 7.7 8.1 9.5 10.1 10.4 L11.4 8.8 L15 10.2 L14.8 12.4 C14.6 13.9 13.4 15 11.9 14.8 C6.6 14.1 1.9 9.4 1.2 4.1 C1 2.6 2.1 1.4 3.6 1.2 Z"/>
        </svg>
      </li>
    </ul>
  </div>
</body>
</html>
```